Pinegate Imaging Group
Mobile ultrasound business cards
Danelle Forbush RDMS, RVT, RT(R)
Owner
418 Whitford Ave. Ste 203-117 Marlow Springs, OR 97388
leave space to add later
danelle_forbush@mailbright.net
There is also a second owner that once design is finalized we will need to edit the text to put her information on the card.
email used on card will need to be changed at a later date!

```html
<!DOCTYPE html>
<html lang="en">
<head>
<meta charset="utf-8">
<title>Pinegate Imaging Group – Business Card</title>
<link rel="stylesheet" href="https://fonts.googleapis.com/css2?family=Cinzel:wght@400;600&display=swap">
<style>
  :root {
    --page-bg: #ecebe8;
    --card-bg: #ffffff;
    --purple: #74368f;
    --purple-deep: #5a2574;
    --purple-light: #9a5bb5;
    --rule-grey: #9a9a9a;
    --ink: #4a3a52;
    --white: #ffffff;
  }
  * { box-sizing: border-box; margin: 0; padding: 0; }
  html, body {
    width: 1200px;
    height: 914px;
    overflow: hidden;
    background: var(--page-bg);
  }
  .canvas {
    width: 1200px;
    height: 914px;
    display: flex;
    align-items: center;
    justify-content: center;
  }
  .card {
    position: relative;
    width: 1050px;
    height: 600px;
    background: var(--card-bg);
    box-shadow: 0 6px 24px rgba(0,0,0,0.12);
    font-family: "Cinzel", "Times New Roman", serif;
  }
  .brand {
    position: absolute;
    top: 120px;
    left: 0;
    right: 0;
    display: flex;
    align-items: center;
    justify-content: center;
    gap: 18px;
  }
  .brand-dot {
    width: 46px;
    height: 46px;
    border-radius: 50%;
    background: var(--purple);
  }
  .brand-name {
    font-size: 38px;
    font-weight: 600;
    color: var(--purple);
    letter-spacing: 1px;
  }
  .band-rule {
    position: absolute;
    left: 0;
    right: 0;
    height: 2px;
    background: var(--rule-grey);
  }
  .band-rule.top { top: 276px; }
  .band-rule.bottom { top: 346px; }
  .band {
    position: absolute;
    top: 282px;
    left: 0;
    right: 0;
    height: 58px;
    background: linear-gradient(90deg, var(--purple-light), var(--purple) 40%, var(--purple-deep));
    display: flex;
    align-items: center;
    justify-content: center;
  }
  .holder {
    color: var(--white);
    font-size: 22px;
    letter-spacing: 1px;
    white-space: nowrap;
  }
  .holder .role { margin-left: 10px; }
  .contacts {
    position: absolute;
    top: 388px;
    left: 60px;
    right: 60px;
    display: flex;
    flex-direction: column;
    gap: 12px;
    color: var(--ink);
    font-size: 17px;
  }
  .contact-row {
    display: flex;
    align-items: center;
    gap: 26px;
    white-space: nowrap;
  }
  .contact-item {
    display: flex;
    align-items: center;
    gap: 8px;
  }
  .icon { width: 20px; height: 20px; flex: none; }
</style>
</head>
<body>
<main class="canvas">
  <section class="card" aria-label="Pinegate Imaging Group business card">
    <header class="brand">
      <span class="brand-dot" aria-hidden="true"></span>
      <span class="brand-name">Pinegate Imaging Group</span>
    </header>

    <div class="band-rule top"></div>
    <div class="band">
      <p class="holder">Danelle Forbush &nbsp;RDMS, RVT, RT(R) <span class="role">| Owner</span></p>
    </div>
    <div class="band-rule bottom"></div>

    <div class="contacts">
      <div class="contact-row">
        <span class="contact-item">
          <svg class="icon" viewBox="0 0 20 20" aria-hidden="true">
            <circle cx="10" cy="10" r="10" fill="#74368f"/>
            <path d="M10 4.5a3.5 3.5 0 0 0-3.5 3.5c0 2.6 3.5 7 3.5 7s3.5-4.4 3.5-7A3.5 3.5 0 0 0 10 4.5zm0 4.8a1.3 1.3 0 1 1 0-2.6 1.3 1.3 0 0 1 0 2.6z" fill="#fff"/>
          </svg>
          418 Whitford Ave. Ste 203-117 Marlow Springs, OR 97388
        </span>
        <span class="contact-item">
          <svg class="icon" viewBox="0 0 20 20" aria-hidden="true">
            <circle cx="10" cy="10" r="10" fill="#74368f"/>
            <path d="M7 5l2 2.6-1.2 1.3a7 7 0 0 0 3.3 3.3l1.3-1.2L15 13l-1.2 1.8c-4 0-8.6-4.6-8.6-8.6z" fill="#fff"/>
          </svg>
          541-555-0183
        </span>
      </div>
      <div class="contact-row">
        <span class="contact-item">
          <svg class="icon" viewBox="0 0 20 20" aria-hidden="true">
            <circle cx="10" cy="10" r="10" fill="#74368f"/>
            <path d="M7 5l2 2.6-1.2 1.3a7 7 0 0 0 3.3 3.3l1.3-1.2L15 13l-1.2 1.8c-4 0-8.6-4.6-8.6-8.6z" fill="#fff"/>
          </svg>
          leave space to add later
        </span>
        <span class="contact-item">
          <svg class="icon" viewBox="0 0 20 20" aria-hidden="true">
            <circle cx="10" cy="10" r="10" fill="#74368f"/>
            <rect x="5" y="6.5" width="10" height="7" fill="none" stroke="#fff" stroke-width="1.3"/>
            <path d="M5 6.5l5 4 5-4" fill="none" stroke="#fff" stroke-width="1.3"/>
          </svg>
          danelle_forbush@mailbright.net
        </span>
      </div>
    </div>
  </section>
</main>
</body>
</html>
```